Landing Page für B2B-Softwareentwicklungsfirma
Zielgruppe
Wir sind eine (relativ kleine) B2B Softwareentwicklungsfirma, die Software zum Wetten auf Pferderennen erstellt.
Unsere Kunden sind Buchmacher und Rennbahnbetreiber.
Unsere Software läuft auf verschiedener Hardware (Touchscreen Terminals, Handy, Kassa, Webseite,...) und wird teilweise von Endkunden (Sportwetter) als auch Kunden-Mitarbeitern verwendet.
Was uns von anderen Softwarefirmen in diesem Bereich unterscheidet ist:
- Wir sind extrem verlässlich und unsere Software läuft störungsfrei
- Wir haben extrem viel Knowhow und ein großes Netzwerk im Bereich Pferdesport/-wetten
- Wir sind flexibel, gehen auf Kundenwünsche immer schnell und kosteneffizient ein
- Unsere softwaretechnischen Fähigkeiten sind ausgezeichnet (wir sind hauptsächlich Programmierer - weniger Businessleute).
- Wir sind für unsere Kunden immer persönlich, direkt und einfach ansprechbar (kleine Firma)
- Wir sind seit ca 15 Jahren erfolgreich im Markt, und auch Marktführer im deutschsprachigen Raum
- Wir haben ein sehr breites Produktportfolio (Terminal, Kassa, Mobile Webseite, Desktop Webseite, Backoffice, Risk Management)
- Wir legen viel Wert auf sauberes und auch modernes UI/UX-Design
Wir benötigen nun einen professionellen Webauftritt um in neue Märkte einzutreten.
Als ersten Schritt möchten wir gerne eine Single-Page Landingpage, die alle wichtigen Punkte im Überblick darstellt.
Aufgabenstellung
Das Design soll die Punkte aus der obigen Beschreibung über uns widerspiegeln, und auch unsere Werte:
Wichtig: Modern, Verlässlichkeit, Dynamisch, Kosteneffizient, Freundlich
Optional: Kreativ, Flexibilität
Wichtig ist auch der Bezug zum Pferderennsport!
Und dass wir eine B2B Softwarefirma sind!
Bitte beachten Sie unser neues Firmenlogo - siehe Anhang.
Die Landingpage soll eher hell, klar, offen, freundlich, sachlich sein.
Die Landingpage soll auf Mobile und Desktop funktionieren und gut aussehen.
Bitte verwenden Sie folgende Gliederung der Landingpage:
Sections:
....* Above the fold
........headline: horse betting software
........subheadline: Multi-product betting solution for bookmakers and racetrack operators.
................................Software production for land-based operations and online betting.
........call-to-action: get in touch
........secondary call-to-action: view products
........switch language
........links to other sections
....* Products
........Point of Sale
............Title: Quick and streamlined bet placement
............Short desc: Optimized bet placement solution for your bet shops and race tracks. Supports Windows-based touchscreen terminals and many different printers and scanners out of the box.
........Self-Service Terminals
............Title: Let users take control
............Short desc: Easy to use touchscreen software for new and professional punters. Running on any Windows-based hardware and adapted to your special needs.
........Web and Mobile Betting
............Title: Reach your target audience wherever they are
............Short desc: Allow your customers to enter their bets on any desktop or mobile browser.
........Bet Management
............Title: Stay in control of your meetings and bets
............Short desc: Browser-based Back-Office solution to control all your meetings,..

```html
<!DOCTYPE html>
<html lang="en">
<head>
<meta charset="utf-8">
<title>tapwerks – Horse Betting Software</title>
<link href="https://fonts.googleapis.com/css2?family=Poppins:wght@400;500;600;700;800&display=swap" rel="stylesheet">
<style>
:root{
  --ink:#24324a;
  --text:#2e3340;
  --brand:#0b5d8c;
  --accent:#2cc7e8;
  --hero-bg:#f4f4f6;
  --page-bg:#fafafb;
  --card-bg:#f6f6f8;
  --rule:#ececf0;
  --device:#24272d;
}
*{margin:0;padding:0;box-sizing:border-box}
html,body{width:671px;height:1200px;overflow:hidden}
body{font-family:'Poppins',sans-serif;background:var(--page-bg);color:var(--text);position:relative}
.abs{position:absolute}
.hero{position:absolute;left:0;top:0;width:671px;height:383px;background:var(--hero-bg)}
.brand-name{left:94px;top:16px;font-size:15px;font-weight:600;letter-spacing:1.5px;color:var(--ink);display:flex;align-items:center;gap:5px}
.brand-name .dot{width:7px;height:7px;border-radius:50%;background:var(--accent)}
.nav a{position:absolute;top:21px;font-size:7px;color:var(--ink);text-decoration:none}
.lang{left:492px;top:21px;font-size:7px;color:var(--ink)}
.btn{position:absolute;display:flex;align-items:center;justify-content:center;background:var(--brand);color:#fff;font-size:7px;font-weight:500;border-radius:3px;box-shadow:0 3px 5px rgba(11,93,140,.25)}
.eyebrow{font-size:7.3px;font-weight:600;letter-spacing:.9px;color:var(--brand)}
.hero h1{left:93px;top:113px;font-size:24px;line-height:28px;font-weight:700;color:var(--ink);white-space:nowrap}
.hero p{left:94px;top:209px;font-size:7.6px;line-height:13.5px;width:200px}
.link{left:198px;top:289px;font-size:7px;font-weight:500;color:var(--brand);text-decoration:underline}
.section-head{left:0;width:671px;text-align:center}
.section-head h2{font-size:20.5px;font-weight:700;color:var(--ink);margin-top:6px}
.section-head p{font-size:7.6px;line-height:12.5px;margin-top:8px}
.mark{width:12px;height:12px;background:var(--accent);border-radius:2px}
.prod-title{font-size:14px;font-weight:700;color:var(--ink)}
.prod-desc{font-size:7.6px;line-height:12.5px;white-space:nowrap}
.feature{position:absolute;width:66px;height:51px;background:var(--card-bg);border-radius:4px;display:flex;flex-direction:column;align-items:center;justify-content:center;gap:6px;font-size:6.8px}
.feature svg{width:15px;height:15px}
.dots{display:flex;gap:5px}
.dots span{width:5px;height:5px;border-radius:50%;background:#e6e6ea}
.dots span:first-child{background:#2a2a2e}
.rule{height:1px;background:var(--rule)}
</style>
</head>
<body>
<section class="hero">
  <div class="abs brand-name"><span>TAPWERKS</span><span class="dot"></span></div>
  <nav class="nav">
    <a style="left:236px">Products ⌄</a>
    <a style="left:282px">Why us?</a>
    <a style="left:327px">Company &amp; Team</a>
    <a style="left:405px">FAQ</a>
  </nav>
  <div class="abs lang">DE / EN</div>
  <div class="btn" style="left:535px;top:15px;width:44px;height:20px">Contact</div>

  <div class="abs eyebrow" style="left:94px;top:96px">HORSE BETTING SOFTWARE PROVIDER</div>
  <h1 class="abs">The Reliable Way<br>To Manage<br>Your Horse Races</h1>
  <p class="abs">We provide multi-product betting solutions for bookmakers and racetrack operators.<br>Our proven software products are a perfect fit for land-based as well as online betting operations.</p>
  <div class="btn" style="left:94px;top:282px;width:88px;height:23px">View our products</div>
  <a class="abs link">Get in touch</a>

  <svg class="abs" style="left:330px;top:60px" width="270" height="280" viewBox="330 60 270 280" role="img" aria-label="Racehorse with jockey leaping over a tablet showing the betting software">
    <defs>
      <linearGradient id="heroTri" x1="0" y1="0" x2="1" y2="1">
        <stop offset="0" stop-color="#35d6f2"/><stop offset="1" stop-color="#1890bd"/>
      </linearGradient>
      <linearGradient id="heroScreen" x1="0" y1="0" x2="1" y2="1">
        <stop offset="0" stop-color="#4c5a6c"/><stop offset="1" stop-color="#2c3644"/>
      </linearGradient>
    </defs>
    <path d="M411 72 Q405 70 407 76 L447 255 L578 132 Q584 127 577 124 Z" fill="url(#heroTri)"/>
    <path d="M384 176 L557 193 Q562 194 561 199 L546 320 Q545 325 540 324 L349 288 Q343 287 345 281 L378 180 Q380 176 384 176 Z" fill="var(--device)"/>
    <path d="M387 183 L552 199 L539 314 L355 281 Z" fill="url(#heroScreen)"/>
  </svg>
</section>

<div class="abs section-head" style="top:429px">
  <div class="eyebrow">BETTING SOLUTIONS</div>
  <h2>Our Products</h2>
  <p>Neque egestas congue quisque egestas diam in. Semper quis<br>lectus nulla at volutpat diam ut venenatis.</p>
</div>

<article>
  <div class="abs mark" style="left:90px;top:563px"></div>
  <h3 class="abs prod-title" style="left:90px;top:577px">Point of Sale</h3>
  <p class="abs prod-desc" style="left:90px;top:607px">Lorem ipsum dolor sit amet, consectetur adipiscing elit, sed do<br>eiusmod tempor incididunt ut labore et dolore magna aliqua.</p>
  <div class="feature" style="left:104px;top:646px"><svg viewBox="0 0 24 24" fill="none" stroke="#b8bcc4" stroke-width="2"><path d="M12 21l-8-8a5 5 0 017-7l1 1 1-1a5 5 0 017 7z"/></svg>100% reliable</div>
  <div class="feature" style="left:178px;top:646px"><svg viewBox="0 0 24 24" fill="none" stroke="#b8bcc4" stroke-width="2"><path d="M7 10v11H3V10zM7 10l4-8a3 3 0 013 3v4h6a2 2 0 012 2l-2 8a2 2 0 01-2 2H7"/></svg>Easy to use</div>
  <div class="feature" style="left:251px;top:646px"><svg viewBox="0 0 24 24" fill="none" stroke="#b8bcc4" stroke-width="2"><path d="M3 17a9 9 0 0118 0M12 17l4-5"/></svg>Performant</div>
  <div class="btn" style="left:90px;top:718px;width:89px;height:22px">More information</div>

  <svg class="abs" style="left:356px;top:546px" width="210" height="180" viewBox="356 546 210 180" role="img" aria-label="Tablet showing the point of sale back office screen">
    <defs>
      <linearGradient id="posScreen" x1="0" y1="0" x2="1" y2="1">
        <stop offset="0" stop-color="#f1f2f5"/><stop offset="1" stop-color="#d3d6dc"/>
      </linearGradient>
    </defs>
    <path d="M368 556 L553 551 Q560 551 560 558 L560 716 Q560 722 553 722 L368 699 Q362 698 362 692 L362 563 Q362 557 368 556 Z" fill="var(--device)"/>
    <path d="M370 566 L549 562 L549 710 L370 690 Z" fill="url(#posScreen)"/>
  </svg>
  <div class="abs dots" style="left:448px;top:736px"><span></span><span></span><span></span></div>
</article>

<div class="abs rule" style="left:90px;top:777px;width:490px"></div>

<article>
  <svg class="abs" style="left:100px;top:843px" width="224" height="136" viewBox="100 843 224 136" role="img" aria-label="Tablet showing the self-service terminal race screen">
    <defs>
      <linearGradient id="sstScreen" x1="0" y1="0" x2="1" y2="1">
        <stop offset="0" stop-color="#3c4a5e"/><stop offset="1" stop-color="#263040"/>
      </linearGradient>
    </defs>
    <path d="M120 847 L303 847 Q309 847 310 853 L319 966 Q319 973 312 973 L112 973 Q105 973 106 966 L114 853 Q115 847 120 847 Z" fill="var(--device)"/>
    <path d="M123 855 L302 855 L309 964 L116 964 Z" fill="url(#sstScreen)"/>
  </svg>
  <div class="abs dots" style="left:197px;top:987px"><span></span><span></span><span></span></div>
  <div class="abs mark" style="left:342px;top:825px"></div>
  <h3 class="abs prod-title" style="left:342px;top:839px">Self-Service Terminals</h3>
  <p class="abs prod-desc" style="left:342px;top:869px">Lorem ipsum dolor sit amet, consectetur adipiscing elit, sed do<br>eiusmod tempor incididunt ut labore et dolore magna aliqua.</p>
  <div class="feature" style="left:354px;top:909px"><svg viewBox="0 0 24 24" fill="none" stroke="var(--accent)" stroke-width="2"><path d="M12 21l-8-8a5 5 0 017-7l1 1 1-1a5 5 0 017 7z"/></svg>100% reliable</div>
  <div class="feature" style="left:427px;top:909px"><svg viewBox="0 0 24 24" fill="none" stroke="var(--accent)" stroke-width="2"><path d="M7 10v11H3V10zM7 10l4-8a3 3 0 013 3v4h6a2 2 0 012 2l-2 8a2 2 0 01-2 2H7"/></svg>Easy to use</div>
  <div class="feature" style="left:501px;top:909px"><svg viewBox="0 0 24 24" fill="none" stroke="var(--accent)" stroke-width="2"><path d="M3 17a9 9 0 0118 0M12 17l4-5"/></svg>Performant</div>
  <div class="btn" style="left:342px;top:984px;width:89px;height:23px">More information</div>
</article>

<div class="abs rule" style="left:85px;top:1061px;width:490px"></div>
</body>
</html>
```